TownDailyo - Business card + Stationery
"Discover fresh corners of your town, daily!" "Today's leading daily deals +"
TownDailyo - Business card + Stationery - Information Technology
Creative Brief
Use specific fonts
Font used is good but open to new ideas
Bright & Fun-filled
Marcus Delwyn
Creator + Director
marcus@towndailyo.example
towndailyo.example
I am looking for a modern catchy design for a new set of business cards. Looking for stationery such as: email template - small logo with web link - Post card - Note pad etc... Looking for a modern design that contains the web link and text to match business card theme. Open to new ideas. Chatterbook and Chirplet logo "TOWNDAILYO" can be used on the cards too. I will make further comments as the various designs come in.
Logo + www. << >>.com on either side of the logo Text at bottom Discover fresh corners of your town, daily

```html
<!DOCTYPE html>
<html lang="en">
<head>
<meta charset="utf-8">
<title>TownDailyo Stationery Set</title>
<link href="https://fonts.googleapis.com/css2?family=Open+Sans:wght@400;600;700&display=swap" rel="stylesheet">
<style>
:root{
  --stage:#2b2b2b;
  --paper:#ffffff;
  --blue:#1f7fc4;
  --blue-dark:#135e98;
  --orange:#f39a1e;
  --ink:#555a60;
  --label:#9a9a9a;
}
*{margin:0;padding:0;box-sizing:border-box}
html,body{width:1200px;height:444px;overflow:hidden;background:var(--stage);font-family:"Open Sans",Arial,sans-serif}
.set{position:relative;width:1200px;height:444px}
.piece{position:absolute;background:var(--paper);overflow:hidden;box-shadow:0 2px 8px rgba(0,0,0,.6)}
.label{position:absolute;font-size:6px;color:var(--label);text-align:center}
.wave{position:absolute;left:0;bottom:0;width:100%}
.brand{display:flex;align-items:center;gap:4px}
.brand-square{width:12px;height:12px;background:var(--orange)}
.brand-name{font-weight:700;color:var(--blue);font-size:11px}
.contact{position:absolute;font-size:5px;line-height:1.5;color:var(--ink)}
.contact strong{color:var(--blue);font-size:6px}
.tagline{font-size:6px;color:var(--orange);font-weight:600}
</style>
</head>
<body>
<main class="set">

  <!-- business card front -->
  <section class="piece card-front" style="left:24px;top:72px;width:173px;height:101px">
    <div class="brand" style="position:absolute;left:12px;top:14px"><span class="brand-square"></span><span class="brand-name">TownDailyo</span></div>
    <div class="contact" style="left:96px;top:12px">
      <strong>Marcus Delwyn</strong><br>Creator + Director<br>+1 555 0142<br>marcus@towndailyo.example<br>towndailyo.example
    </div>
    <svg class="wave" height="34" viewBox="0 0 300 60" preserveAspectRatio="none"><path d="M0 24C90 4 190 54 300 14" fill="none" stroke="var(--orange)" stroke-width="4"/><path d="M0 34C100 10 200 60 300 24V60H0Z" fill="var(--blue)"/></svg>
  </section>
  <p class="label" style="left:24px;top:178px;width:173px">Business Card</p>

  <!-- card back option A -->
  <section class="piece card-back-white" style="left:24px;top:192px;width:173px;height:91px">
    <div class="brand" style="position:absolute;left:12px;top:14px"><span class="brand-square"></span><span class="brand-name">TownDailyo</span></div>
    <p class="tagline" style="position:absolute;left:0;right:0;top:62px;text-align:center">Discover fresh corners of your town, daily!</p>
    <svg class="wave" height="16" viewBox="0 0 300 60" preserveAspectRatio="none"><path d="M0 40C100 10 200 60 300 30V60H0Z" fill="var(--blue)"/></svg>
  </section>
  <p class="label" style="left:24px;top:288px;width:173px">Card Back Option A</p>

  <!-- card back option B -->
  <section class="piece card-back-blue" style="left:24px;top:312px;width:173px;height:91px;background:var(--blue)">
    <div class="brand" style="position:absolute;left:12px;top:14px"><span class="brand-square"></span><span class="brand-name" style="color:#fff">TownDailyo</span></div>
    <p class="tagline" style="position:absolute;left:0;right:0;top:66px;text-align:center;color:#fff">towndailyo.example</p>
    <svg class="wave" height="22" viewBox="0 0 300 60" preserveAspectRatio="none"><path d="M0 34C100 8 200 60 300 20V60H0Z" fill="var(--blue-dark)"/></svg>
  </section>
  <p class="label" style="left:24px;top:408px;width:173px">Card Back Option B</p>

  <!-- letterhead A -->
  <section class="piece letterhead" style="left:216px;top:24px;width:300px;height:408px">
    <div class="brand" style="position:absolute;left:24px;top:22px"><span class="brand-square"></span><span class="brand-name">TownDailyo</span></div>
    <div class="contact" style="left:176px;top:20px">+1 555 0142<br>marcus@towndailyo.example<br>towndailyo.example<br>12 Harbor Lane, Springvale</div>
    <svg class="wave" height="52" viewBox="0 0 300 60" preserveAspectRatio="none"><path d="M0 22C90 2 190 52 300 12" fill="none" stroke="var(--orange)" stroke-width="3"/><path d="M0 32C100 8 200 60 300 22V60H0Z" fill="var(--blue)"/></svg>
  </section>
  <p class="label" style="left:216px;top:435px;width:300px">Letterhead Option A</p>

  <!-- letterhead B -->
  <section class="piece letterhead" style="left:533px;top:24px;width:297px;height:408px">
    <div class="brand" style="position:absolute;left:24px;top:22px"><span class="brand-square"></span><span class="brand-name">TownDailyo</span></div>
    <div class="contact" style="left:124px;bottom:58px;text-align:center">marcus@towndailyo.example<br>towndailyo.example</div>
    <svg class="wave" height="52" viewBox="0 0 300 60" preserveAspectRatio="none"><path d="M0 22C90 2 190 52 300 12" fill="none" stroke="var(--orange)" stroke-width="3"/><path d="M0 32C100 8 200 60 300 22V60H0Z" fill="var(--blue)"/></svg>
  </section>
  <p class="label" style="left:533px;top:435px;width:297px">Letterhead Option B</p>

  <!-- envelope back -->
  <section class="piece envelope-back" style="left:845px;top:108px;width:331px;height:180px;background:#f4f4f4">
    <svg style="position:absolute;inset:0" width="331" height="180" viewBox="0 0 331 180"><path d="M0 0L165 110L331 0" fill="#fff" stroke="#ddd"/><path d="M0 180L130 85M331 180L200 85" stroke="#ddd" fill="none"/></svg>
    <div class="brand" style="position:absolute;left:128px;top:20px"><span class="brand-square"></span><span class="brand-name">TownDailyo</span></div>
    <p class="contact" style="left:0;right:0;top:44px;text-align:center">towndailyo.example</p>
  </section>
  <p class="label" style="left:845px;top:294px;width:331px">Envelope Back</p>

  <!-- envelope front -->
  <section class="piece envelope-front" style="left:845px;top:312px;width:331px;height:108px">
    <div class="brand" style="position:absolute;left:18px;top:14px"><span class="brand-square"></span><span class="brand-name">TownDailyo</span></div>
    <p class="contact" style="left:18px;top:34px">12 Harbor Lane, Springvale</p>
    <svg class="wave" height="34" viewBox="0 0 300 60" preserveAspectRatio="none"><path d="M0 22C90 2 190 52 300 12" fill="none" stroke="var(--orange)" stroke-width="3"/><path d="M0 32C100 8 200 60 300 22V60H0Z" fill="var(--blue)"/></svg>
  </section>
  <p class="label" style="left:845px;top:425px;width:331px">Envelope Front</p>

</main>
</body>
</html>
```